Book cover design for a book named FLINT

Hello Designers,
The name of the book is FLINT and it is about unexpected experiences individuals have which are beyond their control. Occurrences they are unable to overcome or get out of themselves without the help of God. After overcoming these situations they know only God could have done this for them, no one else could have. It is an adult Christian book. I would like you to be as creative as you can with the cover, using color, light, graphic designs, shapes, scale, lines etc. (you are the designers, I don't know how to do these things.) I would like to use the image created on a paperback, hardcover or e book. I tried to use an image from Framelodge just to give you some idea of my thinking but you do not have to use these hands. The hands should look as if they are giving someone the word TESTIMONY not receiving it. Use of the words provided, the light rays, and some type of hands extended should not change, but how you use them is up to you. Use the words, light rays, and hands however you wish as long as they convey someone giving the word TESTIMONY. The word TESTIMONY should be proportional to the hand in size and should appear as if being held in the actual hand it should not be larger than the book name. It is a Christian book of testimonies. Also for your design samples you can use the name Melissa Trent for the author. Thank you, please feel free to contact me if you have any questions. I am looking for the cover to be an attention grabber and give the reader something to really think about and remember visually when they see this cover. Thank you again.

Target Market(s)

anyone and christians

Requirements
Must have
• Use of the words provided, the light rays, and some type of hands extended should not change.
Nice to have
• be as creative as you can with the cover, using color, light, graphic designs, shapes, scale, lines etc. (you are the designers, I don't know how to do these things.)
Should not have
• It should not have fonts, colors, etc. that convey it is a child's book, fairytale, or fictional etc. It is a book of true stories that actually happened. It should not look exactly like my example, what I provided.

```html
<!DOCTYPE html>
<html lang="en">
<head>
<meta charset="utf-8">
<title>FLINT — Book Cover Spread</title>
<link rel="stylesheet" href="https://fonts.googleapis.com/css2?family=Bebas+Neue&family=Noto+Serif:ital@1&family=Tinos&display=swap">
<style>
  :root {
    --page-bg: #f0f0f0;
    --cover-black: #000000;
    --ink-white: #ffffff;
    --gold-dark: #b8893a;
    --gold-mid: #e9c465;
    --gold-light: #fff09a;
    --accent-red: #e8141c;
    --ember-dark: #6a2a08;
    --ember-mid: #e07a10;
    --ember-light: #ffc21e;
  }
  * { margin: 0; padding: 0; box-sizing: border-box; }
  html, body { width: 1200px; height: 1200px; overflow: hidden; background: var(--page-bg); }

  .cover-spread {
    position: absolute; left: 65px; top: 253px; width: 1070px; height: 800px;
    background: var(--cover-black);
    box-shadow: 0 30px 30px -22px rgba(0,0,0,.45);
  }
  .gold-title {
    position: absolute; font-family: "Bebas Neue", sans-serif; line-height: 1;
    background: linear-gradient(90deg, var(--gold-dark) 0%, var(--gold-mid) 25%, var(--gold-light) 55%, var(--gold-mid) 85%, var(--gold-dark) 100%);
    -webkit-background-clip: text; background-clip: text; color: transparent;
    white-space: nowrap;
  }
  .gold-rule {
    position: absolute; height: 1px;
    background: linear-gradient(90deg, transparent, var(--gold-mid) 50%, transparent);
  }

  /* Back cover */
  .back-title { left: 34px; width: 434px; top: 25px; font-size: 128px; text-align: center; }
  .back-rule { left: 44px; width: 406px; top: 157px; }
  .blurb {
    position: absolute; left: 34px; top: 186px; width: 434px;
    font-family: "Tinos", serif; font-size: 11.6px; line-height: 18.3px;
    color: var(--ink-white); text-align: justify;
  }
  .blurb p + p { margin-top: 18.3px; }

  /* Spine */
  .spine-title, .spine-author {
    position: absolute; transform: rotate(90deg); transform-origin: center;
    font-family: "Bebas Neue", sans-serif; line-height: 1; white-space: nowrap;
  }
  .spine-title { left: 470px; top: 168px; width: 200px; text-align: center; font-size: 62px; }
  .spine-author { left: 462px; top: 568px; width: 200px; text-align: center; font-size: 31px; color: var(--ink-white); letter-spacing: .5px; }

  /* Front cover */
  .front-title { left: 620px; width: 413px; top: 22px; font-size: 246px; text-align: center; }
  .tag-rule-top { left: 621px; width: 404px; top: 230px; }
  .tag-rule-bottom { left: 621px; width: 404px; top: 303px; }
  .tagline {
    position: absolute; left: 610px; width: 426px; top: 236px;
    font-family: "Noto Serif", serif; font-style: italic; font-size: 22px; line-height: 31px;
    color: var(--ink-white); text-align: center;
  }
  .tagline em { color: var(--accent-red); font-style: italic; }
  .hands-image {
    position: absolute; left: 581px; top: 337px; width: 478px; height: 366px;
    background:
      radial-gradient(ellipse 22% 20% at 55% 56%, #fffbe6 0%, #fff2a8 35%, rgba(255,220,120,0) 100%),
      radial-gradient(ellipse 48% 42% at 55% 58%, rgba(240,170,110,.85) 0%, rgba(170,80,60,.55) 45%, rgba(60,20,10,0) 100%),
      radial-gradient(ellipse 60% 55% at 55% 50%, rgba(180,140,40,.35) 0%, rgba(0,0,0,0) 100%);
  }
  .hands-caption {
    position: absolute; left: 581px; width: 478px; top: 433px; text-align: center;
    font-family: "Bebas Neue", sans-serif; font-size: 37px; line-height: 1;
    color: var(--ink-white); letter-spacing: -.5px;
  }
  .hands-word {
    position: absolute; left: 581px; width: 478px; top: 478px; text-align: center;
    font-family: "Bebas Neue", sans-serif; font-size: 82px; line-height: 1; letter-spacing: -1px;
    background: linear-gradient(90deg, var(--ember-dark) 0%, var(--ember-mid) 30%, var(--ember-light) 55%, var(--ember-mid) 78%, var(--ember-dark) 100%);
    -webkit-background-clip: text; background-clip: text; color: transparent;
  }
  .front-author {
    position: absolute; left: 620px; width: 413px; top: 728px; text-align: center;
    font-family: "Bebas Neue", sans-serif; font-size: 40px; line-height: 1;
    color: var(--ink-white); letter-spacing: 3px;
  }
</style>
</head>
<body>
  <div class="cover-spread">
    <section class="back-cover">
      <h2 class="gold-title back-title">FLINT</h2>
      <div class="gold-rule back-rule"></div>
      <div class="blurb">
        <p>Most often, we are more than happy to be the recipients of good things freely given to us by God. But when troubling events come into our lives the response can vary from, "why is this happening to me," to feelings of frustration and confusion. Within the pages of this book are testimonies provided by ordinary people that were able, with the help of God, to overcome monumental situations. These are real life events that are easily understood but not always believed by anyone other than the person who experienced them. What's amazing about a testimony is that it can travel everywhere; like bad news or gossip.</p>
        <p>But unlike those scenarios, each story has the ability to create lasting change for personal and eternal good. They are stories that can be discussed everywhere by anyone, touching the heart of the hearer and possibly increasing their faith and drawing them closer to Christ. Every detail of their story was already known by God, allowed by God, and will work together for each person's good. Some of the experiences can bring immediate joy while other experiences have more intensity as a test of one's faith and commitment to God. Some experiences bring a level of discomfort many would sooner reject if there was foreknowledge. In these instances, our minds rationalize it would be better if God didn't permit what was sent. During these times, it is necessary to trust God because He knows the path that will accomplish what is best for each of us. Even when we can't understand how something good could possibly come from the experience, there will come a day when it will be revealed that the experience was actually a blessing God had given.</p>
      </div>
    </section>

    <section class="spine">
      <div class="gold-title spine-title">FLINT</div>
      <div class="spine-author">MELISSA TRENT</div>
    </section>

    <section class="front-cover">
      <h1 class="gold-title front-title">FLINT</h1>
      <div class="gold-rule tag-rule-top"></div>
      <p class="tagline">Before there will ever be a <em>TESTIMONY</em><br>there must always be an experience</p>
      <div class="gold-rule tag-rule-bottom"></div>
      <div class="hands-image" role="img" aria-label="Open outstretched hands offering a burst of golden light rays"></div>
      <div class="hands-caption">OUT OF THE TEST I'VE GIVEN YOU A</div>
      <div class="hands-word">TESTIMONY</div>
      <div class="front-author">MELISSA TRENT</div>
    </section>
  </div>
</body>
</html>
```